Upmarket building and construction company needs signage

Our building company R Brent Construction, needs signage to put up on the side of our vehicle trailers and on site fencing. We are a building company that specialises in residential construction and carpentry .

I will attach our logo and some inspirational pics for site fencing as well as what our trailer looks like .
Other details i would like on the sign are our
( email) rbrentconstruction@mailbox-example.net
(mobile ) 0493 518 264
(website ) rbrentconstruction. example.net

Target Market(s)

Home owners looking for a reliable local builder who produces good quality work. I have attached some inspirational pics.

Industry/Entity Type

Building and Construction

Colors

Designer to choose colors to be used in the design.

Requirements
Must have
• Our logo, contact information
Nice to have
• We would like the design to have elements of being Elegant, Serious, Modern, Professional, Masculine, Conservative and Upmarket.

```html
<!DOCTYPE html>
<html lang="en">
<head>
<meta charset="utf-8">
<title>R Brent Construction – Site Signage</title>
<link rel="stylesheet" href="https://fonts.googleapis.com/css2?family=Jost:wght@300&family=Roboto+Condensed:wght@700&family=Roboto:wght@700&display=swap">
<style>
  :root {
    --backdrop: #cccccc;
    --panel-dark: #545452;
    --panel-shade: #424241;
    --panel-light: #ffffff;
    --ink-dark: #4d4d4d;
    --mark-light: #e4e4e4;
    --ribbon: #444444;
    --ribbon-fold: #222222;
    --text-light: #ffffff;
  }
  * { margin: 0; padding: 0; box-sizing: border-box; }
  html, body {
    width: 1200px; height: 779px; overflow: hidden;
    background: var(--backdrop);
  }
  .sign {
    position: absolute; left: 47px; top: 183px;
    width: 1106px; height: 412px;
    background: var(--panel-light);
    overflow: hidden;
  }
  .brand-panel {
    position: absolute; left: 0; top: 0;
    width: 687px; height: 412px;
    background: var(--panel-dark);
  }
  .brand-decor {
    position: absolute; left: 0; top: 92px;
    width: 223px; height: 320px;
    background: var(--panel-shade);
  }
  .brand-square {
    position: absolute; left: 539px; top: 50px;
    width: 100px; height: 100px;
    background: var(--text-light);
  }
  .brand {
    position: absolute; left: 257px; top: 178px;
    width: 382px;
    font-family: "Jost", sans-serif; font-weight: 300;
    color: var(--text-light);
    text-align: right;
  }
  .brand-name {
    font-size: 96px; line-height: 1; letter-spacing: 1px;
    white-space: nowrap;
  }
  .brand-word {
    font-size: 44px; line-height: 1; letter-spacing: 2.4px;
    margin-top: 20px; white-space: nowrap;
  }
  .brand-tagline {
    font-size: 27px; line-height: 1; letter-spacing: 1.6px;
    margin-top: 15px; white-space: nowrap;
  }
  .contact {
    position: absolute; left: 733px; top: 36px;
    color: var(--ink-dark);
  }
  .call-now {
    font-family: "Roboto Condensed", sans-serif; font-weight: 700;
    font-size: 40px; line-height: 1;
  }
  .phone {
    display: flex; align-items: center; gap: 8px;
    margin-top: 10px;
    font-family: "Roboto", sans-serif; font-weight: 700;
    font-size: 30px; line-height: 1;
  }
  .phone svg { width: 34px; height: 34px; fill: var(--ink-dark); }
  .ribbon {
    position: absolute; left: 675px; top: 135px;
    width: 340px; height: 52px;
  }
  .ribbon-email {
    position: absolute; left: 733px; top: 142px;
    font-family: "Roboto", sans-serif; font-weight: 700;
    font-size: 12.5px; line-height: 17px; letter-spacing: 0.3px;
    color: var(--text-light);
  }
  .website {
    position: absolute; left: 733px; top: 176px;
    font-family: "Roboto", sans-serif; font-weight: 700;
    font-size: 14px; line-height: 18px; letter-spacing: 0.3px;
    color: var(--ink-dark);
    white-space: nowrap;
  }
  .contact-decor {
    position: absolute; left: 699px; top: 210px;
    width: 366px; height: 202px;
    background: var(--mark-light);
  }
</style>
</head>
<body>
  <div class="sign">
    <div class="brand-panel"></div>
    <div class="brand-decor" role="img" aria-label="Large faint brand mark decoration"></div>
    <div class="brand-square" role="img" aria-label="Brand mark placeholder"></div>

    <div class="brand">
      <div class="brand-name">R BRENT</div>
      <div class="brand-word">CONSTRUCTION</div>
      <div class="brand-tagline">BUILDING AND CARPENTRY</div>
    </div>

    <div class="contact">
      <div class="call-now">CALL NOW</div>
      <div class="phone">
        <svg viewBox="0 0 24 24" aria-hidden="true">
          <path d="M6.6 10.8c1.4 2.8 3.8 5.1 6.6 6.6l2.2-2.2c.3-.3.7-.4 1-.2 1.1.4 2.3.6 3.6.6.6 0 1 .4 1 1V20c0 .6-.4 1-1 1C10.6 21 3 13.4 3 4c0-.6.4-1 1-1h3.5c.6 0 1 .4 1 1 0 1.3.2 2.5.6 3.6.1.3 0 .7-.2 1z"/>
          <path d="M14 3.2a7 7 0 0 1 6.8 6.8h-1.6A5.4 5.4 0 0 0 14 4.8zM14 6.4a3.8 3.8 0 0 1 3.6 3.6H16A2.2 2.2 0 0 0 14 8z"/>
        </svg>
        <span>+61 493 518 264</span>
      </div>
    </div>

    <svg class="ribbon" viewBox="0 0 340 52" aria-hidden="true">
      <polygon points="0,30 12,30 12,49" fill="var(--ribbon-fold)"/>
      <polygon points="0,0 336,0 299,30 0,30" fill="var(--ribbon)"/>
    </svg>
    <div class="ribbon-email">rbrentconstruction@mailbox-example.net</div>
    <div class="website">rbrentconstruction. example.net</div>

    <div class="contact-decor" role="img" aria-label="Large brand mark decoration"></div>
  </div>
</body>
</html>
```